Plum Stride Buisiness card

needing a Business card for our company - Plum Stride.
Plum stride is co owned by Nell and Dermot Wardrop (Husband and Wife)
Services Plum Stride provides include:
Dietetic/nutrition Consultations, weight loss coaching programs, personal and group training, post injury rehab, health and nutrition presentations and Health Retreats.
Nell:
Accredited Practicing Dietitian & Personal trainer
Dermot:
Personal trainer, rehab trainer & Strength and conditioning coach
At this stage the business cards will be made just for Nell.
She has a training studio in Armadale and Dietetics private practice in Richmond.
Mobile services are also available (i.e. meet at house or local cafe)

We need the card to look smart, modern and combine both nutrition and training.
We already have a logo which I will attach.
I was initial thinking i black background but am open to suggestions.

Target Market(s)

Health concious, People with money,

Industry/Entity Type

Nutrition

Contact Information for Business Card

Plum Stride
Nell Wardrop
M: 0431907265
E: plumstride@postwren.com
W: www.plumstride.com.au
Address:
Dietetics: Level 1, 88 Tolley Street
Kelsworth VIC 3187
Training: Rear Workroom, behind 517 Merrow St
BRAYFIELD, VIC, 3152

Requirements
Must have
• Must have logo (see attached) please not the one we use is the top left (blue and green)
please note attachment is top left (green and blue)

needs to be clear to read - the font needs to be clear and sharp and the background cannot be too busy.eg funny patterns.
Could I please see a card with a line for 'appointment time/date:' possibly on the back. Would like to see what this looks like.
Nell Wardrop's Profile (side of card) must include "Accredited Practicing Dietitian" and "Personal Trainer."
I like when the services plum stride provide are in dot form.
Nice to have
• would like the card to be 2 sides
first side:
Plum stride logo - Large
services plum stride provides: Dietetic/nutrition Consultations, weight loss coaching programs, personal and group training, post injury rehab, health and nutrition presentations and Health Retreats.
web address
second side:
smaller logo
Details for Nell:
Accredited Practicing Dietitian
Personal Trainer
Contact Details:
M: 0431907265
E: plumstride@postwren.com
Address:
Kelsworth VIC 3187
BRAYFIELD, VIC, 3152
Should not have
• Dietetic + nutrition consultations
Should say dietetic/nutrition consultations (first letter of words in capitals please)
Please write phone number as 0431 907 265
Not: 04 31 907265
- note numbers as 4, 3, 3.

```html
<!DOCTYPE html>
<html lang="en">
<head>
<meta charset="utf-8">
<title>Plum Stride – Business Card</title>
<link href="https://fonts.googleapis.com/css2?family=Open+Sans:ital,wght@0,400;0,600;0,700;1,700&display=swap" rel="stylesheet">
<style>
  :root {
    --brand-blue: #0f55a1;
    --brand-green: #8bbb2f;
    --card-white: #ffffff;
    --text-grey: #3a3a3a;
    --tagline-grey: #6f6f6f;
    --page-bg: #e4e4e4;
  }
  * { margin: 0; padding: 0; box-sizing: border-box; }
  html, body {
    width: 1056px; height: 1200px; overflow: hidden;
    background: var(--page-bg);
    font-family: "Open Sans", Arial, sans-serif;
  }
  .card {
    position: absolute;
    width: 711px; height: 397px;
    background: var(--card-white);
    transform: scale(1.242);
    transform-origin: 0 0;
    overflow: hidden;
    box-shadow: 0 1px 4px rgba(0,0,0,.25);
  }
  .card--front { left: 77px; top: 83px; }
  .card--back  { left: 87px; top: 646px; }
  .card__bands { position: absolute; inset: 0; width: 711px; height: 397px; }
  .band--blue  { fill: var(--brand-blue); }
  .band--green { fill: var(--brand-green); }

  .tilted { position: absolute; transform-origin: 0 0; white-space: nowrap; }

  /* Brand name */
  .brand { display: flex; align-items: center; gap: 8px; }
  .brand__dot {
    width: 26px; height: 26px; border-radius: 50%;
    background: var(--brand-green); flex: none;
  }
  .brand__name {
    font-family: "Open Sans", Arial, sans-serif;
    font-weight: 600; color: var(--brand-blue);
    letter-spacing: -1px; line-height: 1;
  }

  /* Front */
  .front__web {
    left: 112px; top: 56px; transform: rotate(18deg);
    color: var(--card-white); font-weight: 700; font-size: 15px; letter-spacing: .3px;
  }
  .services {
    left: 86px; top: 126px; transform: rotate(18deg);
    list-style: none; color: var(--brand-blue);
    font-size: 13px; line-height: 16.5px; text-transform: uppercase; letter-spacing: .2px;
  }
  .services li { position: relative; }
  .services li::before {
    content: ""; position: absolute; left: -30px; top: 2px;
    width: 4px; height: 4px; border-radius: 50%; background: var(--brand-blue);
  }
  .front__brand { left: 470px; top: 150px; transform: rotate(12deg); }
  .front__brand .brand__name { font-size: 36px; }
  .front__tagline {
    left: 496px; top: 212px; transform: rotate(14deg);
    color: var(--tagline-grey); font-weight: 700; font-style: italic; font-size: 11px;
  }

  /* Back */
  .back__brand { left: 22px; top: 168px; transform: rotate(-9deg); }
  .back__brand .brand__name { font-size: 34px; }
  .profile { left: 318px; top: 74px; transform: rotate(-18deg); color: var(--card-white); }
  .profile__name { font-size: 20px; font-weight: 700; line-height: 28px; }
  .profile__role { font-size: 14.5px; line-height: 24px; }
  .contact { left: 352px; top: 214px; transform: rotate(-18deg); width: 340px; height: 220px; }
  .contact__line {
    position: absolute; left: 0; display: flex; align-items: center; gap: 8px;
    color: var(--brand-blue); font-weight: 700; font-size: 17px;
  }
  .contact__line--phone { top: 0; }
  .contact__line--email { top: 30px; }
  .contact__line svg { width: 16px; height: 16px; flex: none; }
  .address {
    position: absolute; font-size: 13.5px; line-height: 17px; color: var(--text-grey);
  }
  .address--dietetics { left: 74px; top: 66px; }
  .address--training  { left: 84px; top: 136px; }
  .address__label { color: var(--brand-green); font-weight: 700; }
  .address--training .address__label { color: var(--brand-blue); }
</style>
</head>
<body>

<section class="card card--front" aria-label="Front of card">
  <svg class="card__bands" viewBox="0 0 711 397" aria-hidden="true">
    <polygon class="band--blue" points="0,0 468,0 400,200 0,70"/>
    <polygon class="band--green" points="468,0 711,0 711,129 453,45"/>
    <polygon class="band--green" points="400,200 711,301 711,397 333,397"/>
  </svg>

  <div class="tilted front__web">www.plumstride.com.au</div>

  <ul class="tilted services">
    <li>Dietetic/Nutrition Consultations</li>
    <li>Weight Loss Coaching Programs</li>
    <li>Personal and Group Training</li>
    <li>Post Injury Rehab</li>
    <li>Health &amp; Nutrition Presentations<br>and Health Retreats</li>
  </ul>

  <div class="tilted brand front__brand">
    <span class="brand__dot"></span>
    <span class="brand__name">Plum Stride</span>
  </div>
  <div class="tilted front__tagline">«Fuel the way you move!»</div>
</section>

<section class="card card--back" aria-label="Back of card">
  <svg class="card__bands" viewBox="0 0 711 397" aria-hidden="true">
    <polygon class="band--blue" points="711,0 243,0 311,200 711,70"/>
    <polygon class="band--green" points="243,0 0,0 0,129 258,45"/>
    <polygon class="band--green" points="311,200 0,301 0,397 378,397"/>
  </svg>

  <div class="tilted brand back__brand">
    <span class="brand__dot"></span>
    <span class="brand__name">Plum Stride</span>
  </div>

  <div class="tilted profile">
    <div class="profile__name">Nell Wardrop</div>
    <div class="profile__role">Accredited Practicing Dietitian</div>
    <div class="profile__role">Personal Trainer</div>
  </div>

  <div class="tilted contact">
    <div class="contact__line contact__line--phone">
      <svg viewBox="0 0 24 24" aria-hidden="true"><path fill="var(--brand-blue)" d="M6.6 10.8a15.1 15.1 0 0 0 6.6 6.6l2.2-2.2a1 1 0 0 1 1-.25 11.4 11.4 0 0 0 3.6.57 1 1 0 0 1 1 1V20a1 1 0 0 1-1 1A17 17 0 0 1 3 4a1 1 0 0 1 1-1h3.5a1 1 0 0 1 1 1c0 1.250.2 2.450.57 3.57a1 1 0 0 1-.25 1z"/></svg>
      <span>0431 907 265</span>
    </div>
    <div class="contact__line contact__line--email">
      <svg viewBox="0 0 24 24" aria-hidden="true"><rect x="2.5" y="5.5" width="19" height="13" fill="none" stroke="var(--brand-blue)" stroke-width="1.6"/><path d="M2.5 5.5 12 13l9.5-7.5" fill="none" stroke="var(--brand-blue)" stroke-width="1.6"/></svg>
      <span>plumstride@postwren.com</span>
    </div>
    <div class="address address--dietetics">
      <span class="address__label">Dietetics:</span> Suite 4,<br>88 Tolley Street<br>Kelsworth VIC 3187
    </div>
    <div class="address address--training">
      <span class="address__label">Training:</span> Rear Workroom,<br>behind 517 Merrow St<br>BRAYFIELD, VIC, 3152
    </div>
  </div>
</section>

</body>
</html>
```